Willowbrook Haven tri-fold brochure

We are a small assisted living in a home-like environment. Brochure should be warm, heartfelt and include the list of services we provide (see existing brochure). I also want the front picture replaced with stock photo (so no picture of owners). New name to use (instead of Trina) is Dorian Kellsey, and email is kellsey@fernmail.test. Address is same. If you can find better photos, that would be good, all the photos here are dated. We are looking for a more professional design that still conveys warmth, because we are in a home-setting and only care for 9 residents.

Target Market(s)

35-55 year old children looking for an assisted living because their parents are unable to care for them.

Industry/Entity Type

Environment

Contact Information for Business Card

Dorian Kellsey
Willowbrook Haven or Willowbrook Haven Assisted Living
18372 Pinegrove Ln. Conroe, TX 77384
281-555-0187

Requirements
Must have
• List of services offered (feel free to re-word or add/change)
• Be sure to change "Trina/Treena" to Dorian / Dorian Kellsey

```html
<!DOCTYPE html>
<html lang="en">
<head>
<meta charset="utf-8">
<title>Willowbrook Haven – Tri-fold Brochure</title>
<link href="https://fonts.googleapis.com/css2?family=Raleway:wght@400;500;600;700&display=swap" rel="stylesheet">
<style>
  :root {
    --canvas: #414143;
    --gold: #8b7232;
    --gold-deep: #7d6628;
    --charcoal: #3b3b3d;
    --ink: #2c2c2c;
    --paper: #ffffff;
    --fold: #e3e3e3;
  }
  * { box-sizing: border-box; margin: 0; padding: 0; }
  html, body { width: 811px; height: 1200px; overflow: hidden; }
  body { background: var(--canvas); font-family: "Raleway", sans-serif; color: var(--ink); position: relative; }

  .sheet { position: absolute; left: 67px; width: 677px; height: 527px; background: var(--paper); overflow: hidden; }
  .sheet--outside { top: 62px; }
  .sheet--inside { top: 610px; }

  .top-band { position: absolute; left: 0; top: 0; width: 100%; height: 18px; background: var(--gold); z-index: 5; }
  .column { position: absolute; top: 0; height: 100%; width: 226px; }
  .column--1 { left: 0; background: linear-gradient(90deg, #fff 70%, var(--fold)); }
  .column--2 { left: 226px; background: linear-gradient(90deg, #ededed, #fff 25%, #fff 75%, var(--fold)); }
  .column--3 { left: 451px; width: 226px; background: linear-gradient(90deg, #ececec, #fff 25%); }

  .wave { position: absolute; left: 0; top: 0; width: 677px; height: 527px; z-index: 2; }

  .photo { position: absolute; z-index: 1; }
  .photo--round { border-radius: 50%; border: 3px solid var(--charcoal); z-index: 3; }

  .content { position: absolute; z-index: 4; }

  .heading { font-size: 18px; font-weight: 500; color: var(--gold); line-height: 1.25; }
  .heading strong { font-weight: 600; }
  .heading--caps { text-transform: uppercase; font-size: 19px; }
  .heading--single { white-space: nowrap; font-size: 17px; }

  .bullets { list-style: none; font-size: 9.6px; line-height: 12px; }
  .bullets li { position: relative; padding-left: 13px; margin-bottom: 12px; }
  .bullets li::before { content: ""; position: absolute; left: 0; top: 3px; width: 5px; height: 5px; border-radius: 50%; background: var(--gold); }
  .bullets p { margin-top: 12px; }

  .body-copy { font-size: 9.6px; line-height: 12px; }
  .body-copy p { margin-bottom: 12px; }
  .lead { font-size: 13px; font-weight: 600; line-height: 15px; }

  .tagline { font-size: 15px; font-weight: 600; line-height: 19px; text-align: center; }
  .call-out { font-size: 9.6px; font-weight: 700; color: var(--gold); text-align: center; line-height: 12px; }
  .address { font-size: 9.6px; text-align: center; line-height: 12px; }

  .brand-name { font-size: 23px; font-weight: 500; color: var(--ink); text-align: center; white-space: nowrap; line-height: 28px; }
  .brand-ribbon { position: absolute; height: 18px; background: var(--gold); border-radius: 0 9px 9px 0; color: #fff; font-size: 9px; font-weight: 600; line-height: 18px; padding-left: 24px; }

  .promise { color: #fff; text-align: center; font-size: 14.5px; line-height: 16.5px; }
  .promise-rule { height: 1px; background: rgba(255,255,255,.55); margin: 12px auto 8px; width: 170px; }
  .contact-name { color: #fff; font-weight: 700; text-align: center; }
  .contact-phone { color: #fff; text-align: center; }
</style>
</head>
<body>

<section class="sheet sheet--outside">
  <div class="top-band"></div>
  <div class="column column--1"></div>
  <div class="column column--2"></div>
  <div class="column column--3"></div>

  <div class="photo" role="img" aria-label="Photo of an elderly woman with a smiling young caregiver" style="left:0;top:300px;width:226px;height:190px;background:linear-gradient(135deg,#d7cfc8,#b98f80 45%,#f1ede8);"></div>
  <div class="photo" role="img" aria-label="Photo of a nurse in blue scrubs helping an elderly woman in bed" style="left:451px;top:124px;width:226px;height:230px;background:linear-gradient(135deg,#e7edf2,#6f9bc9 45%,#e9dce0);"></div>

  <svg class="wave" viewBox="0 0 677 527" aria-hidden="true">
    <path d="M400,348 C470,320 560,308 677,298 L677,314 C560,320 480,335 420,360 Z" fill="var(--charcoal)"/>
    <path d="M0,424 C90,490 230,505 330,450 C400,405 470,350 560,342 C610,338 650,334 677,332 L677,527 L0,527 Z" fill="var(--gold)"/>
  </svg>

  <div class="photo photo--round" role="img" aria-label="Photo of a smiling grandfather with his daughter and grandson" style="left:237px;top:306px;width:182px;height:182px;background:linear-gradient(135deg,#cfd9e3,#c9a88e 50%,#8e9aa8);"></div>

  <div class="content" style="left:24px;top:40px;width:190px;">
    <h2 class="heading">Testimonials</h2>
    <ul class="bullets" style="margin-top:12px;">
      <li>My mom lived in five private care homes. When she moved to Dorian Kellsey she said, “I’ve finally found my home.”</li>
      <li>“I lived in a facility where everything I seemed to be...door..., door..., door... Here is small, familiar and comfortable”</li>
      <li>“I’d be miserable in a nursing home!” If you are one of the millions of people who feel this way, we say,
        <p>“Trust your instincts”</p>
        <p>Discover that smaller is better where full service care is provided in a real home.</p>
      </li>
    </ul>
  </div>

  <div class="content" style="left:237px;top:40px;width:206px;">
    <h2 class="heading" style="text-align:center;">Smaller <strong>is better When it comes to the elderly</strong></h2>
    <p class="tagline" style="margin-top:16px;">Our unique homes are designed to make the surroundings familiar and the care consistent.</p>
    <p class="call-out" style="margin-top:24px;">Please call for a personal tour and experience the Willowbrook Haven difference.</p>
    <p class="address" style="margin-top:18px;">18372 Pinegrove Ln.<br>Conroe, Texas<br>kellsey@fernmail.test</p>
  </div>

  <div class="content" style="left:451px;top:52px;width:226px;">
    <p class="brand-name">Willowbrook Haven</p>
  </div>
  <div class="brand-ribbon content" style="left:451px;top:96px;width:200px;">Assisted Living &amp; Memory Care</div>

  <div class="content" style="left:463px;top:390px;width:190px;">
    <p class="promise">Offering a true and noble commitment to the highest standards of care in the industry.</p>
    <div class="promise-rule"></div>
    <p class="contact-name" style="font-size:14px;">Dorian Kellsey</p>
    <p class="contact-phone" style="font-size:14px;">281-555-0187</p>
  </div>
</section>

<section class="sheet sheet--inside">
  <div class="top-band"></div>
  <div class="column column--1" style="width:230px;"></div>
  <div class="column column--2" style="left:230px;"></div>
  <div class="column column--3"></div>

  <svg class="wave" viewBox="0 0 677 527" aria-hidden="true">
    <path d="M250,432 C330,400 400,360 453,346 L500,330 C420,350 360,385 262,430 Z" fill="var(--charcoal)"/>
    <path d="M0,360 C70,420 150,440 240,434 C320,428 390,395 460,372 C540,350 620,330 677,318 L677,527 L0,527 Z" fill="var(--gold)"/>
    <path d="M600,430 C640,410 665,395 677,380 L677,395 C660,410 640,425 610,440 Z" fill="var(--charcoal)"/>
  </svg>

  <div class="photo photo--round" role="img" aria-label="Photo of a laughing senior couple embracing" style="left:17px;top:282px;width:205px;height:205px;background:linear-gradient(135deg,#e8e4de,#d9b9a3 50%,#b8b3ad);"></div>
  <div class="photo photo--round" role="img" aria-label="Photo of a smiling mother and adult daughter hugging" style="left:463px;top:292px;width:194px;height:194px;background:linear-gradient(135deg,#f0ece6,#c79a80 50%,#e8e2da);"></div>

  <div class="content" style="left:21px;top:40px;width:205px;">
    <h2 class="heading heading--single">Why <strong>Willowbrook Haven?</strong></h2>
    <div class="body-copy" style="margin-top:10px;">
      <p><span class="lead">Choosing the right place</span><br>for your loved one is an important decision. Willowbrook Haven is here to help give you peace of mind.</p>
      <p>Innovative care in a residential environment provides a wonderful alternative to institutional living. Our residents truly become a family because of the small, intimate, home-like atmosphere.</p>
      <p>Our first concern is making life safe, comfortable and enjoyable for those who have been entrusted to us.</p>
    </div>
  </div>

  <div class="content" style="left:245px;top:40px;width:202px;">
    <h2 class="heading heading--caps"><strong>Services</strong></h2>
    <ul class="bullets" style="margin-top:12px;">
      <li>Medical supervision provided by visiting physicians and nursing personnel</li>
      <li>Rehabilitation, home health and hospice services available through licensed professionals</li>
      <li>Medications and incontinence management</li>
      <li>Personal attention, caregiver involvement and heightened activities focusing on hobbies, crafts, exercise, music therapy, holiday and birthday celebrations, and plant and pet therapy.</li>
      <li>Nutritious home cooked meals and snacks with emphasis on hydration.</li>
      <li>Assistance with bathing, grooming and other personal needs including daily laundry and housekeeping.</li>
    </ul>
  </div>

  <div class="content" style="left:468px;top:40px;width:200px;">
    <h2 class="heading heading--caps">Willowbrook Haven <strong>is your home</strong></h2>
    <div class="body-copy" style="margin-top:10px;">
      <p>The comforts of home in a private luxurious setting, allows loving care with dignity</p>
      <p>Private or companion rooms, elegantly furnished or personalized to your style.</p>
      <p>A living room, family room, dining room, sunroom, and kitchen residents can call their own, so they can live the way they always have.</p>
      <p>Enjoy beautiful days on the patio and in the lovely garden area with beautiful trees, flowers, birds and pets.</p>
    </div>
  </div>

  <div class="content" style="left:230px;top:452px;width:221px;">
    <p class="contact-name" style="font-size:20px;">Dorian Kellsey</p>
    <p class="contact-phone" style="font-size:18px;">281-555-0187</p>
  </div>
</section>

</body>
</html>
```